Valtimore Sciences needs high end Label Design for a revolutionary new supplement

We at Valtimore Sciences are looking for a brand new Label Design for a first of its kind product called Tolmisse. It is the first supplement on the market that treats grief and heartbreak. This product is unisex for both men and woman. We want the New Label to look high end and luxurious using the brand colors which are gold and burgundy. Please feel free to use other colors such as black, white, or gray to go along with it or any other colors if you feel would be a great fit! Valtimore Sciences is like the Quorvel of the supplement world, coming out with new products that will challenge the way people treat different symptoms. To Recap:

1. Product Name: TOLMISSE - the font will play a big roll
2. The Label will be placed on an all white bottle
3. Some parts of the label will be printed with foil to make parts of the label shiny and more attractive. Please keep this in mind when designing.
4. Must use our Logo. I will attach a file of our logo and of the emblem as well. Feel free to use the emblem separately if you have a great idea for it. Please let us know if you need the Logo in a different file type.
5. This all natural herbal supplement in pill form is the first to treat grief and support someone with a broken heart. The consumers purchasing this product will be going through a hard and emotional time. This is a serious product.
6. The manufacturer has included some basic instructions regarding the dye line and file types. Please do your best to meet these. If you cannot meet the guidelines please submit art work anyways. If your design is chosen we will just have the manufacturer replicate the design.

The final label should portray Tolmisse and Valtimore Sciences as a luxurious brand and product which was made with cutting edge science leading the way with revolutionary ideas. We want customers to feel that the product is worth every penny, because it is. As soon as they receive the product and take one look at the label, I want them to think WOW I made the right choice buying this. I have attached some Label designs that we really liked for your review.

Please feel free to message me with any questions or if you need the Logo in a different file type. Thank you all.
Updates

Please send in more entries while we take a couple days to review, we are still looking for that one design we can work with. We are getting close, thank you all!

Target Market(s)

People going through grief and heartbreak.

Font styles to use
Sans Serif
Script
Other font styles liked:
• Any font that looks good, The font for the name TOLMISSE is very important and will brand it. We hated the font used in the label we received in our first label draft (attached so you can see)

Requirements
Must have
• Must have the company Logo that says the company name
• Must have the colors Gold and Burgundy
• Must have some areas that will be the shiny foil when label is printed.
• Must say "Dietary Supplement" somewhere near the bottom along with "90 Capsules"
• I have attached a Label someone designed for us but were not really happy with. I did like the font the "Dietary supplement" and "90 Capsules" had and also where it was placed. We absolutely HATED the font used for Tolmisse.
• Must look at the label design we received from the manufacturer and take into consideration the room needed to write in the directions and all the symbols such as "made in america" and "BQH Facility" Don't worry about adding these in as they will put those in before printing but keep in mind they will be added to the Final Label along with the Supplement Facts.
Nice to have
• Would like to see other colors to go with gold and burgundy suck as black, white, or gray. I have attached some Label designs that I really liked for your reference.
Should not have
• Does not need to have any other legal language, that will be applied by the the manufacturer's graphics team.

```html
<!DOCTYPE html>
<html lang="en">
<head>
<meta charset="utf-8">
<title>Tolmisse Label – Valtimore Sciences</title>
<link rel="stylesheet" href="https://fonts.googleapis.com/css2?family=Cinzel:wght@400;600&family=Cormorant+Garamond:ital,wght@1,500&family=Open+Sans:wght@400;600;700&display=swap">
<style>
  :root {
    --page: #f1f1f1;
    --burgundy: #4a1c19;
    --burgundy-deep: #3a1411;
    --gold-light: #f6d27a;
    --gold: #d49a35;
    --gold-dark: #9a5d1a;
    --crimson: #b3242b;
    --ink: #ffffff;
    --ink-soft: #e9dcd8;
    --plaque-ink: #2a0f0c;
  }
  * { box-sizing: border-box; margin: 0; padding: 0; }
  html, body { width: 1200px; height: 857px; overflow: hidden; background: var(--page); }
  body { font-family: "Open Sans", sans-serif; color: var(--ink); }

  .label {
    position: absolute; left: 30px; top: 180px; width: 1140px; height: 497px;
    background: linear-gradient(180deg, var(--burgundy) 0%, var(--burgundy-deep) 100%);
    display: grid; grid-template-columns: 1fr 1fr 1fr;
  }
  .foil-band {
    position: absolute; left: 0; right: 0; height: 16px;
    background: linear-gradient(90deg, var(--gold-dark), var(--gold-light) 30%, var(--gold) 55%, var(--gold-light) 80%, var(--gold-dark));
  }
  .foil-band--top { top: 0; }
  .foil-band--bottom { bottom: 0; }

  .panel { position: relative; padding: 40px 34px 34px; }

  /* Directions panel */
  .directions p { font-size: 14px; line-height: 1.25; text-align: justify; margin-bottom: 14px; }
  .directions .lead { font-style: italic; font-weight: 600; }
  .warnings { font-size: 13.5px; text-transform: uppercase; line-height: 1.2; margin-bottom: 14px; }
  .disclaimer {
    border: 1px solid var(--ink); padding: 6px 8px; font-size: 11px; line-height: 1.35;
  }
  .badges { display: flex; gap: 12px; margin-top: 26px; align-items: center; }
  .badge { width: 46px; height: 46px; border: 2px solid var(--ink-soft); border-radius: 50%; }
  .badge--flag { width: 30px; height: 40px; border-radius: 4px; background: #c9c9d6; border: none; }
  .badge--shield { border-radius: 6px 6px 22px 22px; background: #cfcfcf; border: none; }

  /* Front panel */
  .front { display: flex; flex-direction: column; align-items: center; padding-top: 52px; }
  .brand { display: flex; flex-direction: column; align-items: center; gap: 14px; }
  .brand-dot { width: 58px; height: 58px; border-radius: 50%; background: var(--gold); }
  .brand-name {
    font-family: "Cinzel", serif; font-weight: 600; color: var(--gold);
    font-size: 24px; letter-spacing: 4px; text-align: center; line-height: 1.1;
  }
  .plaque {
    margin-top: 30px; width: 310px; height: 58px; border-radius: 4px;
    background: linear-gradient(180deg, var(--gold-light), var(--gold) 55%, var(--gold-dark));
    display: flex; align-items: center; justify-content: center;
    border: 2px solid var(--gold-dark);
  }
  .product-name {
    font-family: "Cinzel", serif; font-size: 44px; font-weight: 400; color: var(--plaque-ink); letter-spacing: 1px;
  }
  .count { margin-top: 58px; font-family: "Cormorant Garamond", serif; font-style: italic; font-size: 54px; line-height: 1; }
  .count-unit { font-size: 11px; letter-spacing: 0.5px; margin-top: 2px; }
  .category { margin-top: 30px; font-weight: 700; font-size: 17px; letter-spacing: 0.5px; }

  /* Facts panel */
  .facts { padding-top: 30px; }
  .facts-box { border: 2px solid var(--ink); padding: 4px 6px; }
  .facts-title { font-weight: 700; font-size: 21px; line-height: 1.1; }
  .facts-meta { font-size: 10.5px; border-bottom: 6px solid var(--ink); padding-bottom: 3px; }
  .facts-meta b { font-weight: 700; }
  .facts-head { text-align: right; font-size: 9.5px; font-weight: 700; border-bottom: 1px solid var(--ink); padding: 3px 0; }
  .facts-row { display: flex; justify-content: space-between; font-size: 9.5px; line-height: 1.35; }
  .facts-group { border-bottom: 1px solid var(--ink); padding: 3px 0; }
  .facts-sub { padding-left: 4px; }
  .facts-note { font-size: 8.5px; padding-top: 3px; }
  .other { border: 1px solid var(--ink); margin-top: 8px; padding: 4px 8px; font-size: 9.5px; line-height: 1.35; }
  .questions { margin-top: 10px; background: var(--ink); color: var(--burgundy); text-align: center; font-size: 11px; padding: 2px; }
  .help { font-size: 11px; margin-top: 4px; }
  .email { font-size: 18px; margin-top: 2px; }
</style>
</head>
<body>
  <section class="label">
    <div class="foil-band foil-band--top"></div>

    <div class="panel directions">
      <p><span class="lead">SUGGESTED USE:</span> As dietary supplement take one (1) capsule twice a day. For best results take 20-30 min before a meal or as directed by your healthcare professional.</p>
      <p><span class="lead">CAUTION:</span> Do not exceed recommended dose. Pregnant or nursing mothers, children under the age of 18, and individuals with a known medical condition should consult a physician before using this or any dietary supplement.</p>
      <div class="warnings">
        Keep out of reach of children<br>
        Do not use if safety seals damaged or missing<br>
        Store in a cool, dry place
      </div>
      <div class="disclaimer">These statements have not been evaluated by the BQH. This product is not intended to diagnose, treat, cure or prevent any disease.</div>
      <div class="badges">
        <span class="badge badge--flag"></span>
        <span class="badge badge--shield"></span>
        <span class="badge"></span>
        <span class="badge"></span>
        <span class="badge"></span>
      </div>
    </div>

    <div class="panel front">
      <div class="brand">
        <span class="brand-dot"></span>
        <span class="brand-name">VALTIMORE<br>SCIENCES</span>
      </div>
      <div class="plaque"><span class="product-name">TOLMISSE</span></div>
      <div class="count">90</div>
      <div class="count-unit">CAPSULES</div>
      <div class="category">DIETARY SUPPLEMENT</div>
    </div>

    <div class="panel facts">
      <div class="facts-box">
        <div class="facts-title">Supplement Facts</div>
        <div class="facts-meta"><b>Serving Size:</b> 1 Veggie Capsule<br><b>Servings Per Container:</b> 60</div>
        <div class="facts-head">Amount Per Serving</div>
        <div class="facts-group">
          <div class="facts-row"><span>Zymeva-Pro™</span><span>2500HUT/400 mg</span></div>
          <div class="facts-sub">
            <div class="facts-row"><span>Enzyme Blend:</span></div>
            <div class="facts-row"><span>Fungal Protease from Aspergillus oryzae</span></div>
            <div class="facts-row"><span>Lactobacillus acidophilus</span></div>
            <div class="facts-row"><span>Lactobacillus casei</span></div>
            <div class="facts-row"><span>Lactobacillus plantarum</span></div>
          </div>
        </div>
        <div class="facts-group">
          <div class="facts-row"><span>Bromelain</span><span>90 GDU</span></div>
          <div class="facts-row"><span>Papain</span><span>2670 TU</span></div>
          <div class="facts-row"><span>Fungal Lipase</span><span>1500 FIP</span></div>
          <div class="facts-row"><span>Fungal Lactase</span><span>600 LACU</span></div>
          <div class="facts-row"><span>Alpha Galactosidase</span><span>300 GALU</span></div>
        </div>
        <div class="facts-note">** Daily Value (DV) not established</div>
      </div>
      <div class="other">Other Ingredients: Cellulose (Vegetable Capsule), Vegetable Magnesium Stearate, Silicon Dioxide.</div>
      <div class="questions">Questions about our product?</div>
      <div class="help">We are here to help you! Email our team at</div>
      <div class="email">care@valtimoresci.com</div>
    </div>

    <div class="foil-band foil-band--bottom"></div>
  </section>
</body>
</html>
```